Content marketing firm needs a creative out of the box stationary design

Please take a look to the uploaded logo
I need the whole stationary package which include designs for (business card, letterhead, folder, notepad, company profile, small and big envelop, CD and its cover, key medal, header cover for social media pages "facebook, twitter, linkedin, insgram, google+" and website, favicon for website, E-mail signature, flyer, brochure)
Business

```html
<!DOCTYPE html>
<html lang="en">
<head>
<meta charset="utf-8">
<title>Lumen Copy – Business Card</title>
<link rel="stylesheet" href="https://fonts.googleapis.com/css2?family=Quicksand:wght@500;700&display=swap">
<style>
  :root {
    --backdrop-light: #eeeeee;
    --backdrop-dark: #c9c9c9;
    --card-white: #ffffff;
    --card-blue-light: #5fb6de;
    --card-blue-dark: #1f7fae;
    --ink: #1e1e1e;
    --brand-grey: #3a3a3a;
    --accent-blue: #2a9fd8;
  }
  * { margin: 0; padding: 0; box-sizing: border-box; }
  html, body {
    width: 1200px;
    height: 871px;
    overflow: hidden;
  }
  body {
    background: radial-gradient(ellipse at 40% 30%, var(--backdrop-light), var(--backdrop-dark));
    font-family: "Quicksand", sans-serif;
    position: relative;
  }
  .card {
    position: absolute;
    width: 560px;
    height: 320px;
    left: 320px;
    border-radius: 0 70px 0 70px;
    box-shadow: 0 10px 28px rgba(0, 0, 0, 0.22);
    overflow: hidden;
  }
  .card--back {
    top: 70px;
    background: linear-gradient(135deg, var(--card-blue-light), var(--card-blue-dark));
    display: flex;
    align-items: center;
    justify-content: center;
  }
  .card--front {
    top: 470px;
    background: var(--card-white);
  }
  .brand {
    display: flex;
    align-items: center;
    gap: 12px;
    font-weight: 700;
    letter-spacing: 1px;
    text-transform: uppercase;
  }
  .brand__mark {
    width: 18px;
    height: 18px;
    border-radius: 50%;
  }
  .card--back .brand {
    color: var(--card-white);
    font-size: 40px;
  }
  .card--back .brand__mark { background: var(--card-white); }
  .card--front .brand {
    position: absolute;
    left: 44px;
    top: 50px;
    color: var(--brand-grey);
    font-size: 30px;
  }
  .card--front .brand__mark { background: var(--accent-blue); }
  .contact {
    position: absolute;
    left: 250px;
    top: 160px;
  }
  .contact__name {
    color: var(--accent-blue);
    font-weight: 700;
    font-size: 22px;
    margin: 0 0 10px 36px;
  }
  .contact__list { list-style: none; }
  .contact__item {
    display: flex;
    align-items: center;
    gap: 14px;
    color: var(--ink);
    font-weight: 700;
    font-size: 20px;
    line-height: 30px;
  }
  .contact__icon {
    width: 20px;
    height: 20px;
    fill: none;
    stroke: var(--ink);
    stroke-width: 2;
    stroke-linecap: round;
    stroke-linejoin: round;
  }
  .contact__icon--solid { fill: var(--ink); stroke: none; }
</style>
</head>
<body>
  <section class="card card--back" aria-label="Business card back">
    <div class="brand"><span class="brand__mark"></span>Lumen Copy</div>
  </section>

  <section class="card card--front" aria-label="Business card front">
    <div class="brand"><span class="brand__mark"></span>Lumen Copy</div>

    <div class="contact">
      <p class="contact__name">Name</p>
      <ul class="contact__list">
        <li class="contact__item">
          <svg class="contact__icon contact__icon--solid" viewBox="0 0 24 24" aria-hidden="true">
            <path d="M6.6 10.8a15.1 15.1 0 0 0 6.6 6.6l2.2-2.2a1 1 0 0 1 1-.25 11.4 11.4 0 0 0 3.6.57 1 1 0 0 1 1 1V20a1 1 0 0 1-1 1A17 17 0 0 1 3 4a1 1 0 0 1 1-1h3.5a1 1 0 0 1 1 1c0 1.25.2 2.45.57 3.57a1 1 0 0 1-.25 1z"/>
          </svg>
          Phone number
        </li>
        <li class="contact__item">
          <svg class="contact__icon" viewBox="0 0 24 24" aria-hidden="true">
            <rect x="3" y="5" width="18" height="14" rx="1"/>
            <path d="M3 6l9 7 9-7"/>
          </svg>
          name@lumencopy.com
        </li>
        <li class="contact__item">
          <svg class="contact__icon contact__icon--solid" viewBox="0 0 24 24" aria-hidden="true">
            <path d="M12 2a7 7 0 0 0-7 7c0 5.2 7 13 7 13s7-7.8 7-13a7 7 0 0 0-7-7zm0 9.5A2.5 2.5 0 1 1 12 6.5a2.5 2.5 0 0 1 0 5z"/>
          </svg>
          Address
        </li>
      </ul>
    </div>
  </section>
</body>
</html>
```